business cards

we want our logos on the back
the information on it are on the design I've uploaded
come up with whatever you think is best, we want something professional, sophisticated and sleek.

```html
<!DOCTYPE html>
<html lang="en">
<head>
<meta charset="utf-8">
<title>Summit Health and Performance – Business Card</title>
<link rel="stylesheet" href="https://fonts.googleapis.com/css2?family=Roboto:wght@300;400;500;700&display=swap">
<style>
  :root {
    --page: #e8e3da;
    --card: #141414;
    --card-edge: #1f1f1f;
    --sand: #d9ccb6;
    --green: #3fa535;
  }
  * { margin: 0; padding: 0; box-sizing: border-box; }
  html, body {
    width: 1200px;
    height: 1046px;
    overflow: hidden;
    background: var(--page);
    font-family: "Roboto", Arial, sans-serif;
  }
  .canvas {
    position: relative;
    width: 1200px;
    height: 1046px;
  }
  .business-card {
    position: absolute;
    left: 60px;
    top: 228px;
    width: 1080px;
    height: 591px;
    border-radius: 34px;
    background: linear-gradient(135deg, var(--card-edge) 0%, var(--card) 55%);
    color: var(--sand);
  }
  .brand {
    position: absolute;
    right: 37px;
    top: 62px;
    text-align: right;
  }
  .brand-name {
    display: flex;
    align-items: center;
    justify-content: flex-end;
    gap: 14px;
    font-size: 20px;
    font-weight: 400;
    letter-spacing: 4px;
    color: var(--sand);
    white-space: nowrap;
  }
  .brand-dot {
    width: 14px;
    height: 14px;
    border-radius: 50%;
    background: var(--sand);
  }
  .brand-services {
    margin-top: 14px;
    font-size: 10.5px;
    font-weight: 500;
    letter-spacing: 0.4px;
    color: var(--green);
    white-space: nowrap;
  }
  .person {
    position: absolute;
    right: 37px;
    top: 205px;
    text-align: right;
  }
  .person-name {
    font-size: 44px;
    line-height: 48px;
    color: var(--green);
    font-weight: 400;
  }
  .person-name .first { font-weight: 700; }
  .person-role {
    font-size: 22px;
    line-height: 30.5px;
    font-weight: 400;
  }
  .contact {
    position: absolute;
    right: 37px;
    top: 406px;
    text-align: right;
  }
  .address {
    font-size: 22px;
    line-height: 30px;
    margin-bottom: 12px;
  }
  .contact-line {
    display: flex;
    align-items: center;
    justify-content: flex-end;
    gap: 14px;
    font-size: 22px;
    line-height: 32px;
    letter-spacing: 0.6px;
  }
  .contact-line.email { font-size: 20px; letter-spacing: 0.2px; }
  .contact-icon { width: 22px; height: 22px; flex: none; }
</style>
</head>
<body>
<main class="canvas">
  <section class="business-card">
    <header class="brand">
      <div class="brand-name"><span class="brand-dot"></span>SUMMIT HEALTH AND PERFORMANCE</div>
      <div class="brand-services">PHYSIO · S&amp;C · COACHING · PERSONAL TRAINING · REHAB · RECOVERY</div>
    </header>

    <div class="person">
      <h1 class="person-name"><span class="first">Mark</span> Delaney</h1>
      <p class="person-role">DIRECTOR</p>
      <p class="person-role">SENIOR PHYSIOTHERAPIST</p>
      <p class="person-role">BHlthSc, MPhysioPrac, MExSc(S&amp;C)</p>
      <p class="person-role">ASCA Level 2</p>
    </div>

    <div class="contact">
      <p class="address">27 Fenwick Rd, Brookvale</p>
      <p class="contact-line">03 9555 0142
        <svg class="contact-icon" viewBox="0 0 24 24" aria-label="Phone" role="img">
          <path fill="var(--green)" d="M6.6 10.8c1.4 2.8 3.8 5.1 6.6 6.6l2.2-2.2c.3-.3.7-.4 1-.2 1.1.4 2.3.6 3.6.6.6 0 1 .4 1 1V20c0 .6-.4 1-1 1C10.6 21 3 13.4 3 4c0-.6.4-1 1-1h3.5c.6 0 1 .4 1 1 0 1.3.2 2.5.6 3.6.1.3 0 .7-.2 1l-2.3 2.2z"/>
          <path fill="none" stroke="var(--green)" stroke-width="1.6" d="M14 3.5a7 7 0 0 1 6.5 6.5M14 7a3.5 3.5 0 0 1 3 3"/>
        </svg>
      </p>
      <p class="contact-line">03 9555 0187
        <svg class="contact-icon" viewBox="0 0 24 24" aria-label="Fax" role="img">
          <rect x="2" y="8" width="5" height="14" rx="1" fill="var(--green)"/>
          <rect x="8" y="10" width="14" height="12" rx="1.5" fill="var(--green)"/>
          <rect x="10" y="2" width="9" height="7" fill="none" stroke="var(--green)" stroke-width="1.6"/>
          <g fill="var(--card)">
            <rect x="10.5" y="13" width="2" height="2"/><rect x="14" y="13" width="2" height="2"/><rect x="17.5" y="13" width="2" height="2"/>
            <rect x="10.5" y="17" width="2" height="2"/><rect x="14" y="17" width="2" height="2"/><rect x="17.5" y="17" width="2" height="2"/>
          </g>
        </svg>
      </p>
      <p class="contact-line email">mark@summithealthperformance.com.au
        <svg class="contact-icon" viewBox="0 0 24 24" aria-label="Email" role="img">
          <path fill="var(--green)" d="M2 10l10-7 10 7v11a1 1 0 0 1-1 1H3a1 1 0 0 1-1-1V10z"/>
          <path fill="none" stroke="var(--card)" stroke-width="1.4" d="M2.5 10.5l9.5 6.5 9.5-6.5M3 21.5l7-5.5M21 21.5l-7-5.5"/>
          <circle cx="12" cy="10" r="2.4" fill="none" stroke="var(--card)" stroke-width="1.2"/>
        </svg>
      </p>
    </div>
  </section>
</main>
</body>
</html>
```